The Willow Cove Clinic - Instagram Photospot

We are looking for an instagram type wal for our pediatric dental office. We are thinking it could be weaved into a whole bunch of what we do (i.e. potentially water marked or faded in the background on letterhead, as an instragram type wall in the practice, as a banner or section of the home page on the website, on rack cards, etc.) I’m thinking it would utilize a nice fun cursive script for the wording "The Willow Cove Clinic is the spot for...." and a bunch of different sized “spots” with meaningful words that speak to who we are. That list would include things like:

• Fun
• Smiles
• Laughter
• Caring
• Comfort
• Amazing
• Kids
• Toddlers
• Teens
• Friends
• Family
• Health
• Education
• Cheer
• Positivity
• Exceptional Care

From a color perspective….we could look at a couple of options. We could have one version that has it washed out and in the background (more subliminal). We could have one version that was consistent with the colors in our logo. And we could have one version that popped with more color by utilizing the colors in some of the artwork we use throughout the office (snowboard picture as an example)

Target Market(s)

Appeal to hip families with kids

Industry/Entity Type

Pediatric Dental

Other font styles liked:
• something modern, hip, playful and fun

Colors
0054AA
0677BA
7BADD7
CADEEF
E8F1F8
0094D4
00A9DD
6FCCEA
C7EBF8
E9F6FB
00AB8E
00BBA5
67D7C9
C6EFE9
E9F9F6

Requirements
Must have
• Use of existing logo and a play on "spots" or polka dots with symbpolic wording. Must appeal to young parents and kiddos (including hip teens)
Should not have
• SHOULDNT BE OVER THE TOP KIDS.

```html
<!DOCTYPE html>
<html lang="en">
<head>
<meta charset="utf-8">
<title>The Willow Cove Clinic – Photospot</title>
<link rel="stylesheet" href="https://fonts.googleapis.com/css2?family=Parisienne&family=Yellowtail&display=swap">
<style>
  :root {
    --navy: #0054AA;
    --ocean: #0677BA;
    --dusk: #7BADD7;
    --mist: #CADEEF;
    --sky: #0094D4;
    --bright-sky: #00A9DD;
    --aqua: #6FCCEA;
    --ice: #C7EBF8;
    --frost: #E9F6FB;
    --sea: #00AB8E;
    --lagoon: #00BBA5;
    --mint: #67D7C9;
    --ink: #0B4A72;
    --white: #FFFFFF;
  }
  * { margin: 0; padding: 0; box-sizing: border-box; }
  html, body { width: 675px; height: 1200px; overflow: hidden; }
  body { background: var(--bright-sky); }
  .photospot {
    position: relative;
    width: 675px;
    height: 1200px;
    overflow: hidden;
    background: linear-gradient(180deg, var(--sea) 0%, #00A9C4 55%, var(--bright-sky) 100%);
  }
  .headline {
    position: absolute;
    left: 0; right: 0;
    text-align: center;
    font-family: "Parisienne", cursive;
    color: var(--ice);
    text-shadow: 0 2px 3px rgba(0, 60, 80, 0.35);
    line-height: 1;
  }
  .headline__name { top: 78px; font-size: 58px; }
  .headline__tail { top: 190px; font-size: 62px; }
  .spot {
    position: absolute;
    left: calc(var(--x) * 1px - var(--r) * 1px);
    top: calc(var(--y) * 1px - var(--r) * 1px);
    width: calc(var(--r) * 2px);
    height: calc(var(--r) * 2px);
    border-radius: 50%;
    background: var(--fill);
    box-shadow: 2px 4px 6px rgba(0, 40, 70, 0.35);
    display: flex;
    align-items: center;
    justify-content: center;
    text-align: center;
    font-family: "Yellowtail", cursive;
    font-size: var(--fs, 36px);
    line-height: 0.95;
    color: var(--text, var(--white));
  }
  .spot--dark-text { --text: var(--ink); }
  .spot--brand { --fs: 40px; color: var(--frost); }
</style>
</head>
<body>
<main class="photospot">
  <h1 class="headline headline__name">The Willow Cove Clinic</h1>
  <p class="headline headline__tail">is the spot for....</p>

  <!-- decorative dots -->
  <span class="spot" style="--x:171;--y:48;--r:19;--fill:var(--ice)"></span>
  <span class="spot" style="--x:97;--y:195;--r:22;--fill:var(--dusk)"></span>
  <span class="spot" style="--x:568;--y:211;--r:19;--fill:var(--dusk)"></span>
  <span class="spot" style="--x:494;--y:362;--r:19;--fill:var(--ice)"></span>
  <span class="spot" style="--x:627;--y:424;--r:22;--fill:var(--sky)"></span>
  <span class="spot" style="--x:49;--y:461;--r:31;--fill:var(--bright-sky)"></span>
  <span class="spot" style="--x:230;--y:564;--r:22;--fill:var(--ice)"></span>
  <span class="spot" style="--x:562;--y:554;--r:19;--fill:var(--dusk)"></span>
  <span class="spot" style="--x:56;--y:601;--r:22;--fill:var(--navy)"></span>
  <span class="spot" style="--x:207;--y:674;--r:22;--fill:var(--sky)"></span>
  <span class="spot" style="--x:589;--y:801;--r:31;--fill:var(--navy)"></span>
  <span class="spot" style="--x:377;--y:893;--r:31;--fill:var(--aqua)"></span>
  <span class="spot" style="--x:49;--y:938;--r:25;--fill:var(--lagoon)"></span>
  <span class="spot" style="--x:616;--y:1002;--r:31;--fill:var(--aqua)"></span>
  <span class="spot" style="--x:438;--y:1013;--r:22;--fill:var(--lagoon)"></span>
  <span class="spot" style="--x:281;--y:1117;--r:31;--fill:var(--lagoon)"></span>

  <!-- brand spot -->
  <div class="spot spot--brand" style="--x:338;--y:431;--r:122;--fill:var(--navy)">Willow Cove</div>

  <!-- word spots -->
  <div class="spot spot--dark-text" style="--x:109;--y:353;--r:69;--fill:var(--ice);--fs:40px">Toddlers</div>
  <div class="spot spot--dark-text" style="--x:579;--y:311;--r:58;--fill:var(--ice);--fs:40px">Health</div>
  <div class="spot" style="--x:552;--y:464;--r:37;--fill:var(--navy);--fs:32px">Fun</div>
  <div class="spot" style="--x:138;--y:536;--r:56;--fill:var(--lagoon);--fs:38px">Smiles</div>
  <div class="spot spot--dark-text" style="--x:299;--y:630;--r:53;--fill:var(--dusk);--fs:38px">Teens</div>
  <div class="spot spot--dark-text" style="--x:464;--y:594;--r:50;--fill:var(--aqua);--fs:38px">Kids</div>
  <div class="spot" style="--x:589;--y:663;--r:62;--fill:var(--dusk);--fs:40px;--text:var(--navy)">Caring</div>
  <div class="spot" style="--x:94;--y:718;--r:72;--fill:var(--sea);--fs:38px">Laughter</div>
  <div class="spot" style="--x:444;--y:731;--r:66;--fill:var(--sky);--fs:40px">Friends</div>
  <div class="spot spot--dark-text" style="--x:298;--y:794;--r:72;--fill:var(--mint);--fs:38px">Positivity</div>
  <div class="spot" style="--x:156;--y:874;--r:72;--fill:var(--bright-sky);--fs:38px">Amazing</div>
  <div class="spot" style="--x:513;--y:922;--r:79;--fill:var(--lagoon);--fs:42px">Education</div>
  <div class="spot spot--dark-text" style="--x:306;--y:984;--r:59;--fill:var(--aqua);--fs:42px">Cheer</div>
  <div class="spot spot--dark-text" style="--x:134;--y:1068;--r:94;--fill:var(--mint);--fs:42px">Exceptional<br>Care</div>
  <div class="spot" style="--x:413;--y:1116;--r:69;--fill:var(--sky);--fs:42px">Comfort</div>
  <div class="spot" style="--x:586;--y:1109;--r:59;--fill:var(--sea);--fs:40px">Family</div>
</main>
</body>
</html>
```